Blue Heron IT Business Card - Clean, Simple

Need a simple, clean standard sized business card for an IT consulting business using existing logo and company colours. Background should be mainly white. Feel free to be creative but clean, simple, quiet design is preferred. Font is specified in logo but any sans serif fonts work.

Contact Information for card is as follows (doesn't need to be in this exact order):

Martin Calloway
Owner
martin@blueheronit.ca
705-391-2586
www.blueheronit.ca

Target Market(s)

Small to medium sized business.

Industry/Entity Type

IT Consulting

Contact Information for Business Card

Logo and contact info.

Font styles to use
Sans Serif

Colors
EE7325
F08F49
F5BC92
FAE3D3
FDF4ED

Requirements
Must have
• All white or mostly white background.

```html
<!DOCTYPE html>
<html lang="en">
<head>
<meta charset="utf-8">
<title>Blue Heron IT Business Card</title>
<link href="https://fonts.googleapis.com/css2?family=Montserrat:wght@400;500;600;700&display=swap" rel="stylesheet">
<style>
  :root {
    --backdrop: #adadad;
    --brand-orange: #ee7325;
    --brand-orange-deep: #d86a2f;
    --paper: #ffffff;
    --ink: #2b2b2b;
  }
  * { margin: 0; padding: 0; box-sizing: border-box; }
  html, body {
    width: 1200px;
    height: 1000px;
    overflow: hidden;
    background: var(--backdrop);
    font-family: "Montserrat", Arial, sans-serif;
  }
  .canvas { position: relative; width: 1200px; height: 1000px; }
  .card {
    position: absolute;
    left: 294px;
    width: 613px;
    height: 352px;
    overflow: hidden;
  }
  .card--front { top: 93px; background: var(--brand-orange); }
  .card--back { top: 529px; background: var(--paper); }

  .front-wordmark {
    position: absolute;
    left: 46px;
    top: 56px;
    color: var(--paper);
    font-weight: 500;
    font-size: 36px;
    letter-spacing: -0.5px;
    line-height: 1;
  }
  .front-decoration {
    position: absolute;
    left: 300px;
    top: 30px;
    width: 313px;
    height: 322px;
  }

  .contact {
    position: absolute;
    left: 58px;
    top: 158px;
    color: var(--ink);
  }
  .contact__name {
    color: var(--brand-orange);
    font-weight: 700;
    font-size: 22px;
    letter-spacing: 0.3px;
    line-height: 1.1;
  }
  .contact__role {
    font-weight: 700;
    font-size: 16px;
    margin-top: 2px;
  }
  .contact__lines {
    margin-top: 18px;
    font-size: 16.5px;
    font-weight: 500;
    line-height: 22px;
    letter-spacing: 0.4px;
  }
  .contact__web {
    margin-top: 21px;
    color: var(--brand-orange);
    font-weight: 700;
    font-size: 16.5px;
    letter-spacing: 0.3px;
  }
  .back-wordmark {
    position: absolute;
    right: 46px;
    top: 276px;
    color: var(--ink);
    font-weight: 500;
    font-size: 31px;
    letter-spacing: -0.5px;
    line-height: 1;
  }
</style>
</head>
<body>
  <main class="canvas">
    <section class="card card--front">
      <div class="front-wordmark">Blue Heron IT</div>
      <svg class="front-decoration" role="img" aria-label="Large faint brand symbol decoration" viewBox="0 0 313 322">
        <defs>
          <radialGradient id="decoFade" cx="65%" cy="70%" r="70%">
            <stop offset="0" stop-color="var(--brand-orange-deep)" stop-opacity="0.7"/>
            <stop offset="1" stop-color="var(--brand-orange-deep)" stop-opacity="0"/>
          </radialGradient>
        </defs>
        <rect width="313" height="322" fill="url(#decoFade)"/>
      </svg>
    </section>

    <section class="card card--back">
      <div class="contact">
        <div class="contact__name">Martin Calloway</div>
        <div class="contact__role">Owner</div>
        <div class="contact__lines">
          <div class="contact__phone">705-391-2586</div>
          <div class="contact__email">martin@blueheronit.ca</div>
        </div>
        <div class="contact__web">www.blueheronit.ca</div>
      </div>
      <div class="back-wordmark">Blue Heron IT</div>
    </section>
  </main>
</body>
</html>
```